Website Required for Small Cyber Security Company

Require a website for Cyber Security company. I have logo which i will attach. Please use logo blue and white as a guide
Would ultimately like the site to have a technology theme with the following pages Landing page
Services
Contact
Careers

I can provide content for each of those pages in due course, until then happy for you to use dummy data to display purposes

Target Market(s)

Government

Industry/Entity Type

Cyber Security

Coding

Coded - Design and coding required

Number of Pages Required

4 page

Colors
0054AA
0677BA
7BADD7
CADEEF
E8F1F8

Requirements
Must have
• High quality finish and UX
Nice to have
• look and feel professional and not cheap

```html
<!DOCTYPE html>
<html lang="en">
<head>
<meta charset="utf-8">
<title>Halden Ridge Consulting</title>
<link href="https://fonts.googleapis.com/css2?family=Open+Sans:wght@400;600;700&display=swap" rel="stylesheet">
<style>
:root{
  --blue-deep:#0054AA;
  --blue:#0677BA;
  --blue-mid:#7BADD7;
  --blue-pale:#CADEEF;
  --blue-ice:#E8F1F8;
  --ink:#000;
  --white:#fff;
  --navy:#06122a;
}
*{margin:0;padding:0;box-sizing:border-box}
html,body{width:1200px;height:2189px;overflow:hidden;background:var(--white);font-family:"Open Sans",sans-serif;color:var(--white)}
.board{position:relative;width:1200px;height:2189px}
.panel{position:absolute;top:41px;width:559px;height:2108px;background:var(--ink);overflow:hidden}
.panel--a{left:27px}
.panel--b{left:614px}
.abs{position:absolute}
.center{transform:translateX(-50%);text-align:center}

/* header */
.hero-bg{left:0;top:0;width:559px;height:320px;background:radial-gradient(ellipse at 40% 10%,#12508f 0%,#0a2c5c 35%,#041226 70%,#000 100%)}
.panel--b .hero-bg{background:radial-gradient(ellipse at 60% 40%,#0d1f3a 0%,#050c1a 55%,#000 100%)}
.brand{left:45px;top:14px;display:flex;align-items:center;gap:6px;font-weight:600;font-size:10px;letter-spacing:.5px;color:var(--white)}
.brand-dot{width:22px;height:22px;border:2px solid var(--blue);border-radius:50%}
.nav{top:26px;font-size:7.5px;color:var(--white);letter-spacing:.2px}
.phone-btn{left:418px;top:20px;width:96px;height:21px;border-radius:11px;background:var(--blue);display:flex;align-items:center;justify-content:center;gap:6px;font-size:7.5px}
.hero-title{left:45px;top:90px;width:300px;font-size:21px;line-height:26px;font-weight:600}
.hero-text{left:45px;top:176px;width:260px;font-size:6.6px;line-height:14.5px}
.btn{height:21px;border-radius:11px;background:var(--blue);display:flex;align-items:center;justify-content:center;gap:5px;font-size:6.8px;font-weight:600;letter-spacing:.3px}
.hero-mark{left:330px;top:85px;width:190px;height:190px;border:3px solid var(--blue);border-radius:50%;display:flex;align-items:center;justify-content:center;font-size:15px;font-weight:600;color:var(--white);text-align:center;line-height:20px}

/* section headings */
.sec-dot{width:20px;height:20px;border:2px solid var(--blue);border-radius:50%;transform:translateX(-50%)}
.sec-title{font-size:15px;font-weight:700;white-space:nowrap;display:flex;align-items:center;gap:8px}
.sec-title .accent{color:var(--blue)}
.sec-title::before,.sec-title::after{content:"";width:20px;height:1.5px;background:var(--blue)}
.intro{left:75px;top:426px;width:409px;font-size:6.8px;line-height:14.5px;text-align:center}

/* services */
.svc{width:124px;text-align:center}
.svc svg{display:block;margin:0 auto 14px;width:30px;height:28px}
.svc-title{font-size:8px;font-weight:600;line-height:14.5px;margin-bottom:5px}
.svc-text{font-size:6.6px;line-height:13.6px}
.read-more{display:inline-block;margin-top:8px;font-size:7px;font-weight:600;text-decoration:underline}
.divider{width:1px;background:var(--white);opacity:.85}

/* why */
.why-bg{left:0;top:875px;width:559px;height:262px;background:radial-gradient(ellipse at 30% 20%,#1c2546 0%,#0b1029 45%,#000 100%)}
.panel--b .why-bg{background:linear-gradient(180deg,#000 0%,#0a1c32 35%,#0a1626 70%,#000 100%)}
.why{width:116px;text-align:center}
.why-ring{width:60px;height:60px;margin:0 auto 12px;border-radius:50%;background:var(--white);border:3px solid var(--blue);box-shadow:0 0 0 2px #0b1a33;display:flex;align-items:center;justify-content:center}
.why-title{font-size:8px;font-weight:600;margin-bottom:4px}
.why-text{font-size:6.6px;line-height:14px}

/* about/tech */
.feature-icon{width:46px;height:46px;border-radius:50%;background:#1b1b1b;display:flex;align-items:center;justify-content:center}
.feature-title{font-size:9px;font-weight:600;letter-spacing:.3px}
.feature-text{font-size:6.6px;line-height:14.5px;width:150px}

.world{left:0;top:1300px;width:559px;height:295px;background:radial-gradient(ellipse at 50% 110%,#0d2a55 0%,#081a38 40%,#000 80%)}

/* consulting */
.photo-arc{left:62px;top:1634px;width:192px;height:192px;border-radius:50%;border-right:4px solid var(--blue);border-top:3px solid var(--blue);border-bottom:3px solid var(--blue);border-left:3px solid transparent}
.photo{left:64px;top:1636px;width:180px;height:180px;border-radius:50%;background:radial-gradient(circle at 65% 40%,#3a6f9a 0%,#1c3655 40%,#0c1628 80%)}
.consult-title{left:298px;top:1648px;display:flex;align-items:center;gap:6px;font-size:12px;font-weight:600;white-space:nowrap}
.consult-title::after{content:"";width:22px;height:1.5px;background:var(--blue)}
.consult-text{left:288px;top:1677px;width:230px;font-size:6.6px;line-height:14.4px}

/* footer */
.foot-bg{left:0;top:1880px;width:559px;height:228px;background:radial-gradient(ellipse at 50% 60%,#0e1522 0%,#000 80%)}
.foot-brand{left:280px;top:1885px;transform:translateX(-50%);display:flex;flex-direction:column;align-items:center;gap:6px;font-size:13px;font-weight:600;letter-spacing:.5px}
.foot-brand .brand-dot{width:34px;height:34px}
.foot-nav{top:1965px;font-size:7.5px}
.contact-icon{width:19px;height:19px;border-radius:50%;background:var(--blue);display:flex;align-items:center;justify-content:center}
.contact-label{font-size:7px;font-weight:600}
.contact-text{font-size:7px;line-height:14.5px}
.copy{left:280px;top:2049px;font-size:6.8px;white-space:nowrap}
.copy .accent{color:var(--blue)}
.social{top:2073px;width:13px;height:13px;border-radius:50%;background:var(--blue)}
</style>
</head>
<body>
<div class="board">

<!-- Panel A -->
<section class="panel panel--a">
  <div class="abs hero-bg" role="img" aria-label="Glowing blue hexagonal network grid background"></div>
  <div class="abs brand"><span class="brand-dot"></span>HALDEN RIDGE</div>
  <nav>
    <span class="abs nav" style="left:209px">HOME</span>
    <span class="abs nav" style="left:257px">SERVICES</span>
    <span class="abs nav" style="left:314px">CONTACT</span>
    <span class="abs nav" style="left:373px">CAREERS</span>
  </nav>
  <div class="abs phone-btn"><svg width="8" height="8" viewBox="0 0 24 24"><path fill="#fff" d="M6.6 10.8a15 15 0 0 0 6.6 6.6l2.2-2.2a1 1 0 0 1 1-.25 11.4 11.4 0 0 0 3.6.57 1 1 0 0 1 1 1V20a1 1 0 0 1-1 1A17 17 0 0 1 3 4a1 1 0 0 1 1-1h3.5a1 1 0 0 1 1 1c0 1.25.2 2.45.57 3.57a1 1 0 0 1-.25 1z"/></svg>+1 555 010 2030</div>
  <h1 class="abs hero-title">Safeguarding the Nation's Digital Assets with Tailored Cybersecurity Solutions.</h1>
  <p class="abs hero-text">At Halden Ridge Consulting, we are an indigenous and veteran-owned firm. Our deep commitment to cybersecurity excellence ensures the highest level of service for our customers.</p>
  <a class="abs btn" style="left:47px;top:226px;width:84px">LEARN MORE <svg width="8" height="8" viewBox="0 0 24 24"><path fill="#fff" d="M12 4l-1.4 1.4 5.6 5.6H4v2h12.2l-5.6 5.6L12 20l8-8z"/></svg></a>
  <div class="abs hero-mark">HALDEN<br>RIDGE</div>

  <div class="abs sec-dot" style="left:280px;top:366px"></div>
  <h2 class="abs sec-title center" style="left:280px;top:396px">OUR <span class="accent">SERVICES</span></h2>
  <p class="abs intro">Lorem ipsum dolor sit amet, consectetur adipiscing elit, sed do eiusmod tempor incididunt ut labore et dolore magna aliqua. Ut enim ad minim veniam, quis nostrud exercitation ullamco laboris nisi ut aliquip ex ea commodo consequat.</p>

  <div class="abs svc" style="left:67px;top:476px"><svg viewBox="0 0 30 28" fill="none" stroke="#0677BA" stroke-width="1.2"><rect x="10" y="12" width="10" height="9" rx="1"/><path d="M12 12V9a3 3 0 0 1 6 0v3"/><circle cx="15" cy="15" r="9.5"/></svg><div class="svc-title">Services Governance Risk and Compliance</div><div class="svc-text">Specializing in ISM and PSPF Harness the power of our deep-rooted expertise in Governance Risk and Compliance.</div><span class="read-more">Read More</span></div>
  <div class="abs divider" style="left:210px;top:478px;height:154px"></div>
  <div class="abs svc" style="left:218px;top:476px"><svg viewBox="0 0 30 28" fill="none" stroke="#0677BA" stroke-width="1.2"><rect x="3" y="3" width="24" height="17" rx="1"/><path d="M11 25h8M15 20v5"/><circle cx="14" cy="11" r="4"/><path d="M17 14l4 4"/></svg><div class="svc-title">Vulnerability Scanning</div><div class="svc-text">Every digital landscape is susceptible to unseen threats. Our vulnerability scanning service delves deep.</div><span class="read-more">Read More</span></div>
  <div class="abs divider" style="left:360px;top:478px;height:154px"></div>
  <div class="abs svc" style="left:368px;top:476px"><svg viewBox="0 0 30 28" fill="none" stroke="#0677BA" stroke-width="1.2"><circle cx="17" cy="8" r="5"/><circle cx="17" cy="8" r="2"/><path d="M3 20h6l6 3 10-4M3 17h5l5 1"/></svg><div class="svc-title">Essential 8 Uplift and Maintenance</div><div class="svc-text">In the constantly evolving domain of cybersecurity, staying up-to-date is paramount. The Essential 8 framework offers a robust. foundation</div><span class="read-more">Read More</span></div>

  <div class="abs svc" style="left:137px;top:669px"><svg viewBox="0 0 30 28" fill="none" stroke="#0677BA" stroke-width="1.2"><rect x="3" y="3" width="24" height="17" rx="1"/><path d="M11 25h8M15 20v5"/><rect x="8" y="7" width="10" height="9"/></svg><div class="svc-title">Digital Landscape<br>Our Culture</div><div class="svc-text">At Halden Ridge Consulting, we're more than just a team; we're a community. Our roots as an indigenous and veteran-owned</div><span class="read-more">Read More</span></div>
  <div class="abs divider" style="left:280px;top:673px;height:153px"></div>
  <div class="abs svc" style="left:298px;top:669px"><svg viewBox="0 0 30 28" fill="none" stroke="#0677BA" stroke-width="1.2"><rect x="3" y="3" width="22" height="17" rx="1"/><path d="M3 7h22M11 11l-3 3 3 3M17 11l3 3-3 3"/><circle cx="24" cy="22" r="3"/></svg><div class="svc-title">Code Review</div><div class="svc-text">Code is the backbone of all digital operations, and its integrity is non-negotiable. Our Code Review service meticulously.</div><span class="read-more">Read More</span></div>

  <div class="abs why-bg" role="img" aria-label="Flowing dotted digital wave pattern"></div>
  <div class="abs sec-dot" style="left:280px;top:910px"></div>
  <h2 class="abs sec-title center" style="left:280px;top:940px">WHY WORK <span class="accent">WITH US?</span></h2>
  <div class="abs why" style="left:39px;top:983px"><div class="why-ring"><svg width="26" height="26" viewBox="0 0 24 24" fill="none" stroke="#0677BA" stroke-width="1.3"><rect x="5" y="3" width="12" height="16" rx="1"/><path d="M8 7h6M8 10h6M8 13h3"/><circle cx="16" cy="16" r="3"/><path d="M18 18l3 3"/></svg></div><div class="why-title">Transparency</div><div class="why-text">Full transparancy of all rates and contracts.</div></div>
  <div class="abs why" style="left:162px;top:983px"><div class="why-ring"><svg width="26" height="26" viewBox="0 0 24 24" fill="none" stroke="#0677BA" stroke-width="1.3"><circle cx="16" cy="8" r="4"/><circle cx="16" cy="8" r="1.5"/><circle cx="7" cy="7" r="2"/><path d="M7 9v6l-2 5M7 15l2 5M4 12h6"/></svg></div><div class="why-title">Challenging Projects</div><div class="why-text">Dive into intricate cybersecurity challenges.</div></div>
  <div class="abs why" style="left:285px;top:983px"><div class="why-ring"><svg width="26" height="26" viewBox="0 0 24 24" fill="none" stroke="#0677BA" stroke-width="1.3"><circle cx="12" cy="13" r="8"/><path d="M8 11l4-2 4 2-4 2zM9 12v3l3 1 3-1v-3M19 2v5M17 4l2-2 2 2"/></svg></div><div class="why-title">Continuous Learning</div><div class="why-text">The cybersecurity landscape is ever-evolving.</div></div>
  <div class="abs why" style="left:408px;top:983px"><div class="why-ring"><svg width="26" height="26" viewBox="0 0 24 24" fill="none" stroke="#0677BA" stroke-width="1.3"><circle cx="12" cy="6" r="2.5"/><circle cx="5" cy="12" r="2"/><circle cx="19" cy="12" r="2"/><path d="M8 13a4 4 0 0 1 8 0M2 19a3 3 0 0 1 6 0M16 19a3 3 0 0 1 6 0M8 19a4 4 0 0 1 8 0"/></svg></div><div class="why-title">Inclusive Environment</div><div class="why-text">Our strength lies in our diversity.</div></div>

  <div class="abs feature-icon" style="left:72px;top:1179px"><svg width="22" height="22" viewBox="0 0 24 24" fill="#0677BA"><circle cx="12" cy="8" r="4"/><path d="M4 21a8 8 0 0 1 16 0z"/></svg></div>
  <h3 class="abs feature-title" style="left:107px;top:1182px">ABOUT US</h3>
  <p class="abs feature-text" style="left:107px;top:1202px">Lorem ipsum dolor sit amet, consectetur elit, sed do eiusmod tempor incididunt ut labore et dolore magna aliqua. Ut enim ad ullamco laboris nisi ut aliquip ex consequat.</p>
  <a class="abs btn" style="left:107px;top:1271px;width:85px">LEARN MORE <svg width="8" height="8" viewBox="0 0 24 24"><path fill="#fff" d="M12 4l-1.4 1.4 5.6 5.6H4v2h12.2l-5.6 5.6L12 20l8-8z"/></svg></a>
  <div class="abs feature-icon" style="left:311px;top:1179px"><svg width="22" height="22" viewBox="0 0 24 24" fill="none" stroke="#0677BA" stroke-width="1.6"><rect x="3" y="3" width="7" height="6"/><rect x="14" y="3" width="7" height="6"/><rect x="8" y="15" width="8" height="6"/><path d="M6 9v3h12V9M12 12v3"/></svg></div>
  <h3 class="abs feature-title" style="left:372px;top:1182px">TECHNOLOGY</h3>
  <p class="abs feature-text" style="left:372px;top:1202px">Lorem ipsum dolor sit amet, consectetur elit, sed do eiusmod tempor incididunt ut labore et dolore magna aliqua. Ut enim ad ullamco laboris nisi ut aliquip ex consequat.</p>
  <a class="abs btn" style="left:372px;top:1271px;width:85px">LEARN MORE <svg width="8" height="8" viewBox="0 0 24 24"><path fill="#fff" d="M12 4l-1.4 1.4 5.6 5.6H4v2h12.2l-5.6 5.6L12 20l8-8z"/></svg></a>

  <div class="abs world" role="img" aria-label="Glowing wireframe globe with world map network"></div>

  <div class="abs photo-arc"></div>
  <div class="abs photo" role="img" aria-label="Photo of an analyst working at monitors in a dark security operations room"></div>
  <h2 class="abs consult-title"><span class="brand-dot" style="width:18px;height:18px"></span>HALDEN RIDGE CONSULTING</h2>
  <p class="abs consult-text">Lorem ipsum dolor sit amet, consectetur adipiscing elit, sed do eiusmod tempor incididunt ut labore et dolore magna aliqua. Ut enim ad minim veniam, quis nostrud exercitation ullamco laboris nisi ut aliquip ex ea commodo consequat. Duis aute irure dolor in reprehenderit in voluptate velit esse cillum dolore eu fugiat nulla pariatur. Excepteur sint occaecat cupidatat non proident, sunt in culpa qui officia deserunt mollit anim id est laborum.</p>
  <a class="abs btn" style="left:288px;top:1788px;width:85px">LEARN MORE <svg width="8" height="8" viewBox="0 0 24 24"><path fill="#fff" d="M12 4l-1.4 1.4 5.6 5.6H4v2h12.2l-5.6 5.6L12 20l8-8z"/></svg></a>

  <footer>
    <div class="abs foot-bg" role="img" aria-label="Faint dotted network constellation backdrop"></div>
    <div class="abs foot-brand"><span class="brand-dot"></span>HALDEN RIDGE</div>
    <span class="abs foot-nav" style="left:183px">HOME</span>
    <span class="abs foot-nav" style="left:230px">SERVICES</span>
    <span class="abs foot-nav" style="left:287px">CONTACT</span>
    <span class="abs foot-nav" style="left:346px">CAREERS</span>
    <div class="abs contact-icon" style="left:60px;top:2000px"><svg width="8" height="8" viewBox="0 0 24 24"><path fill="#fff" d="M6.6 10.8a15 15 0 0 0 6.6 6.6l2.2-2.2a1 1 0 0 1 1-.25 11.4 11.4 0 0 0 3.6.57 1 1 0 0 1 1 1V20a1 1 0 0 1-1 1A17 17 0 0 1 3 4a1 1 0 0 1 1-1h3.5a1 1 0 0 1 1 1c0 1.25.2 2.45.57 3.57a1 1 0 0 1-.25 1z"/></svg></div>
    <div class="abs" style="left:92px;top:1996px"><div class="contact-label">PHONE:</div><div class="contact-text">+1 555 010 2030</div></div>
    <div class="abs contact-icon" style="left:204px;top:2000px"><svg width="8" height="8" viewBox="0 0 24 24"><path fill="#fff" d="M2 5h20v14H2zM2 6l10 7 10-7" /></svg></div>
    <div class="abs" style="left:236px;top:1996px"><div class="contact-label">EMAIL:</div><div class="contact-text">info@haldenridge.example</div></div>
    <div class="abs contact-icon" style="left:388px;top:2000px"><svg width="8" height="8" viewBox="0 0 24 24"><path fill="#fff" d="M12 2a7 7 0 0 0-7 7c0 5 7 13 7 13s7-8 7-13a7 7 0 0 0-7-7zm0 9.5A2.5 2.5 0 1 1 12 6.5a2.5 2.5 0 0 1 0 5z"/></svg></div>
    <div class="abs" style="left:420px;top:1996px"><div class="contact-label">ADDRESS:</div><div class="contact-text">Halden Ridge Consulting,<br>United State.</div></div>
    <p class="abs copy center">Copyrights@2023.<span class="accent">Halden Ridge Consulting</span>.All Rights Reserved</p>
    <span class="abs social" style="left:246px"></span>
    <span class="abs social" style="left:265px"></span>
    <span class="abs social" style="left:284px"></span>
    <span class="abs social" style="left:303px"></span>
  </footer>
</section>

<!-- Panel B -->
<section class="panel panel--b">
  <div class="abs hero-bg" role="img" aria-label="Dark background with faint dotted digital wave"></div>
  <div class="abs brand"><span class="brand-dot"></span>HALDEN RIDGE</div>
  <nav>
    <span class="abs nav" style="left:209px">HOME</span>
    <span class="abs nav" style="left:257px">SERVICES</span>
    <span class="abs nav" style="left:314px">CONTACT</span>
    <span class="abs nav" style="left:373px">CAREERS</span>
  </nav>
  <div class="abs phone-btn"><svg width="8" height="8" viewBox="0 0 24 24"><path fill="#fff" d="M6.6 10.8a15 15 0 0 0 6.6 6.6l2.2-2.2a1 1 0 0 1 1-.25 11.4 11.4 0 0 0 3.6.57 1 1 0 0 1 1 1V20a1 1 0 0 1-1 1A17 17 0 0 1 3 4a1 1 0 0 1 1-1h3.5a1 1 0 0 1 1 1c0 1.25.2 2.45.57 3.57a1 1 0 0 1-.25 1z"/></svg>+1 555 010 2030</div>
  <h1 class="abs hero-title" style="top:98px">Safeguarding the Nation's Digital Assets with Tailored Cybersecurity Solutions.</h1>
  <p class="abs hero-text" style="top:184px">At Halden Ridge Consulting, we are an indigenous and veteran-owned firm. Our deep commitment to cybersecurity excellence ensures the highest level of service for our customers.</p>
  <a class="abs btn" style="left:47px;top:234px;width:84px">LEARN MORE <svg width="8" height="8" viewBox="0 0 24 24"><path fill="#fff" d="M12 4l-1.4 1.4 5.6 5.6H4v2h12.2l-5.6 5.6L12 20l8-8z"/></svg></a>
  <div class="abs hero-mark" style="left:335px;top:93px">HALDEN<br>RIDGE</div>

  <div class="abs sec-dot" style="left:280px;top:366px"></div>
  <h2 class="abs sec-title center" style="left:280px;top:396px">OUR <span class="accent">SERVICES</span></h2>
  <p class="abs intro">Lorem ipsum dolor sit amet, consectetur adipiscing elit, sed do eiusmod tempor incididunt ut labore et dolore magna aliqua. Ut enim ad minim veniam, quis nostrud exercitation ullamco laboris nisi ut aliquip ex ea commodo consequat.</p>

  <div class="abs svc" style="left:67px;top:476px"><svg viewBox="0 0 30 28" fill="none" stroke="#0677BA" stroke-width="1.2"><rect x="10" y="12" width="10" height="9" rx="1"/><path d="M12 12V9a3 3 0 0 1 6 0v3"/><circle cx="15" cy="15" r="9.5"/></svg><div class="svc-title">Services Governance Risk and Compliance</div><div class="svc-text">Specializing in ISM and PSPF Harness the power of our deep-rooted expertise in Governance Risk and Compliance.</div><span class="read-more">Read More</span></div>
  <div class="abs divider" style="left:210px;top:478px;height:154px"></div>
  <div class="abs svc" style="left:218px;top:476px"><svg viewBox="0 0 30 28" fill="none" stroke="#0677BA" stroke-width="1.2"><rect x="3" y="3" width="24" height="17" rx="1"/><path d="M11 25h8M15 20v5"/><circle cx="14" cy="11" r="4"/><path d="M17 14l4 4"/></svg><div class="svc-title">Vulnerability Scanning</div><div class="svc-text">Every digital landscape is susceptible to unseen threats. Our vulnerability scanning service delves deep.</div><span class="read-more">Read More</span></div>
  <div class="abs divider" style="left:360px;top:478px;height:154px"></div>
  <div class="abs svc" style="left:368px;top:476px"><svg viewBox="0 0 30 28" fill="none" stroke="#0677BA" stroke-width="1.2"><circle cx="17" cy="8" r="5"/><circle cx="17" cy="8" r="2"/><path d="M3 20h6l6 3 10-4M3 17h5l5 1"/></svg><div class="svc-title">Essential 8 Uplift and Maintenance</div><div class="svc-text">In the constantly evolving domain of cybersecurity, staying up-to-date is paramount. The Essential 8 framework offers a robust. foundation</div><span class="read-more">Read More</span></div>

  <div class="abs svc" style="left:137px;top:669px"><svg viewBox="0 0 30 28" fill="none" stroke="#0677BA" stroke-width="1.2"><rect x="3" y="3" width="24" height="17" rx="1"/><path d="M11 25h8M15 20v5"/><rect x="8" y="7" width="10" height="9"/></svg><div class="svc-title">Digital Landscape<br>Our Culture</div><div class="svc-text">At Halden Ridge Consulting, we're more than just a team; we're a community. Our roots as an indigenous and veteran-owned</div><span class="read-more">Read More</span></div>
  <div class="abs divider" style="left:280px;top:673px;height:153px"></div>
  <div class="abs svc" style="left:298px;top:669px"><svg viewBox="0 0 30 28" fill="none" stroke="#0677BA" stroke-width="1.2"><rect x="3" y="3" width="22" height="17" rx="1"/><path d="M3 7h22M11 11l-3 3 3 3M17 11l3 3-3 3"/><circle cx="24" cy="22" r="3"/></svg><div class="svc-title">Code Review</div><div class="svc-text">Code is the backbone of all digital operations, and its integrity is non-negotiable. Our Code Review service meticulously.</div><span class="read-more">Read More</span></div>

  <div class="abs why-bg" role="img" aria-label="Dark field of glowing translucent cubes"></div>
  <div class="abs sec-dot" style="left:280px;top:910px"></div>
  <h2 class="abs sec-title center" style="left:280px;top:940px">WHY WORK <span class="accent">WITH US?</span></h2>
  <div class="abs why" style="left:39px;top:983px"><div class="why-ring"><svg width="26" height="26" viewBox="0 0 24 24" fill="none" stroke="#0677BA" stroke-width="1.3"><rect x="5" y="3" width="12" height="16" rx="1"/><path d="M8 7h6M8 10h6M8 13h3"/><circle cx="16" cy="16" r="3"/><path d="M18 18l3 3"/></svg></div><div class="why-title">Transparency</div><div class="why-text">Full transparancy of all rates and contracts.</div></div>
  <div class="abs why" style="left:162px;top:983px"><div class="why-ring"><svg width="26" height="26" viewBox="0 0 24 24" fill="none" stroke="#0677BA" stroke-width="1.3"><circle cx="16" cy="8" r="4"/><circle cx="16" cy="8" r="1.5"/><circle cx="7" cy="7" r="2"/><path d="M7 9v6l-2 5M7 15l2 5M4 12h6"/></svg></div><div class="why-title">Challenging Projects</div><div class="why-text">Dive into intricate cybersecurity challenges.</div></div>
  <div class="abs why" style="left:285px;top:983px"><div class="why-ring"><svg width="26" height="26" viewBox="0 0 24 24" fill="none" stroke="#0677BA" stroke-width="1.3"><circle cx="12" cy="13" r="8"/><path d="M8 11l4-2 4 2-4 2zM9 12v3l3 1 3-1v-3M19 2v5M17 4l2-2 2 2"/></svg></div><div class="why-title">Continuous Learning</div><div class="why-text">The cybersecurity landscape is ever-evolving.</div></div>
  <div class="abs why" style="left:408px;top:983px"><div class="why-ring"><svg width="26" height="26" viewBox="0 0 24 24" fill="none" stroke="#0677BA" stroke-width="1.3"><circle cx="12" cy="6" r="2.5"/><circle cx="5" cy="12" r="2"/><circle cx="19" cy="12" r="2"/><path d="M8 13a4 4 0 0 1 8 0M2 19a3 3 0 0 1 6 0M16 19a3 3 0 0 1 6 0M8 19a4 4 0 0 1 8 0"/></svg></div><div class="why-title">Inclusive Environment</div><div class="why-text">Our strength lies in our diversity.</div></div>

  <div class="abs feature-icon" style="left:72px;top:1179px"><svg width="22" height="22" viewBox="0 0 24 24" fill="#0677BA"><circle cx="12" cy="8" r="4"/><path d="M4 21a8 8 0 0 1 16 0z"/></svg></div>
  <h3 class="abs feature-title" style="left:107px;top:1182px">ABOUT US</h3>
  <p class="abs feature-text" style="left:107px;top:1202px">Lorem ipsum dolor sit amet, consectetur elit, sed do eiusmod tempor incididunt ut labore et dolore magna aliqua. Ut enim ad ullamco laboris nisi ut aliquip ex consequat.</p>
  <a class="abs btn" style="left:107px;top:1271px;width:85px">LEARN MORE <svg width="8" height="8" viewBox="0 0 24 24"><path fill="#fff" d="M12 4l-1.4 1.4 5.6 5.6H4v2h12.2l-5.6 5.6L12 20l8-8z"/></svg></a>
  <div class="abs feature-icon" style="left:311px;top:1179px"><svg width="22" height="22" viewBox="0 0 24 24" fill="none" stroke="#0677BA" stroke-width="1.6"><rect x="3" y="3" width="7" height="6"/><rect x="14" y="3" width="7" height="6"/><rect x="8" y="15" width="8" height="6"/><path d="M6 9v3h12V9M12 12v3"/></svg></div>
  <h3 class="abs feature-title" style="left:372px;top:1182px">TECHNOLOGY</h3>
  <p class="abs feature-text" style="left:372px;top:1202px">Lorem ipsum dolor sit amet, consectetur elit, sed do eiusmod tempor incididunt ut labore et dolore magna aliqua. Ut enim ad ullamco laboris nisi ut aliquip ex consequat.</p>
  <a class="abs btn" style="left:372px;top:1271px;width:85px">LEARN MORE <svg width="8" height="8" viewBox="0 0 24 24"><path fill="#fff" d="M12 4l-1.4 1.4 5.6 5.6H4v2h12.2l-5.6 5.6L12 20l8-8z"/></svg></a>

  <div class="abs world" role="img" aria-label="Glowing wireframe globe with world map network"></div>

  <div class="abs photo-arc"></div>
  <div class="abs photo" role="img" aria-label="Photo of an analyst working at monitors in a dark security operations room"></div>
  <h2 class="abs consult-title"><span class="brand-dot" style="width:18px;height:18px"></span>HALDEN RIDGE CONSULTING</h2>
  <p class="abs consult-text">Lorem ipsum dolor sit amet, consectetur adipiscing elit, sed do eiusmod tempor incididunt ut labore et dolore magna aliqua. Ut enim ad minim veniam, quis nostrud exercitation ullamco laboris nisi ut aliquip ex ea commodo consequat. Duis aute irure dolor in reprehenderit in voluptate velit esse cillum dolore eu fugiat nulla pariatur. Excepteur sint occaecat cupidatat non proident, sunt in culpa qui officia deserunt mollit anim id est laborum.</p>
  <a class="abs btn" style="left:288px;top:1788px;width:85px">LEARN MORE <svg width="8" height="8" viewBox="0 0 24 24"><path fill="#fff" d="M12 4l-1.4 1.4 5.6 5.6H4v2h12.2l-5.6 5.6L12 20l8-8z"/></svg></a>

  <footer>
    <div class="abs foot-bg" role="img" aria-label="Faint dotted network constellation backdrop"></div>
    <div class="abs foot-brand"><span class="brand-dot"></span>HALDEN RIDGE</div>
    <span class="abs foot-nav" style="left:183px">HOME</span>
    <span class="abs foot-nav" style="left:230px">SERVICES</span>
    <span class="abs foot-nav" style="left:287px">CONTACT</span>
    <span class="abs foot-nav" style="left:346px">CAREERS</span>
    <div class="abs contact-icon" style="left:60px;top:2000px"><svg width="8" height="8" viewBox="0 0 24 24"><path fill="#fff" d="M6.6 10.8a15 15 0 0 0 6.6 6.6l2.2-2.2a1 1 0 0 1 1-.25 11.4 11.4 0 0 0 3.6.57 1 1 0 0 1 1 1V20a1 1 0 0 1-1 1A17 17 0 0 1 3 4a1 1 0 0 1 1-1h3.5a1 1 0 0 1 1 1c0 1.25.2 2.45.57 3.57a1 1 0 0 1-.25 1z"/></svg></div>
    <div class="abs" style="left:92px;top:1996px"><div class="contact-label">PHONE:</div><div class="contact-text">+1 555 010 2030</div></div>
    <div class="abs contact-icon" style="left:204px;top:2000px"><svg width="8" height="8" viewBox="0 0 24 24"><path fill="#fff" d="M2 5h20v14H2zM2 6l10 7 10-7" /></svg></div>
    <div class="abs" style="left:236px;top:1996px"><div class="contact-label">EMAIL:</div><div class="contact-text">info@haldenridge.example</div></div>
    <div class="abs contact-icon" style="left:388px;top:2000px"><svg width="8" height="8" viewBox="0 0 24 24"><path fill="#fff" d="M12 2a7 7 0 0 0-7 7c0 5 7 13 7 13s7-8 7-13a7 7 0 0 0-7-7zm0 9.5A2.5 2.5 0 1 1 12 6.5a2.5 2.5 0 0 1 0 5z"/></svg></div>
    <div class="abs" style="left:420px;top:1996px"><div class="contact-label">ADDRESS:</div><div class="contact-text">Halden Ridge Consulting,<br>United State.</div></div>
    <p class="abs copy center">Copyrights@2023.<span class="accent">Halden Ridge Consulting</span>.All Rights Reserved</p>
    <span class="abs social" style="left:246px"></span>
    <span class="abs social" style="left:265px"></span>
    <span class="abs social" style="left:284px"></span>
    <span class="abs social" style="left:303px"></span>
  </footer>
</section>

</div>
</body>
</html>
```